【概要】 求人サイトに掲載するサムネイル画像作成依頼です。 素敵なデザインがあれば複数採用いたします。 【 依頼内容 】 ・サイズ:横900x縦600 ・ターゲット:20代~50代向けの求人 【 入れていただきたい文言】※これ以外の文言は入れないでください ・固定ルート+体力負担なし+無理な運転はさせない社風=長く働ける環境です! ・6tドライバー募集 ・月給35万円可能 【画像に関して】 注:こちらの画像サイズ、データで提出できる方のみお願い致します。 ★「横900ピクセルx縦600ピクセル」(PNGファイル×1、PSDデータ×1) ・配信時は制作したバナーがスマホの画面幅程度に縮小されて表示されます。テキストの可読性を考慮して制作お願いします。 ・文字を記入する際、できれば画像としてではなく、フォトショップのテキストを使用していただければと存じます。 ・テキストデータはアウトライン化されていない、後から編集できる状態での納品をお願いいたします。(イラストレーターNG) ・フォントやあしらいにフリー素材を使用する場合は著作権に抵触しないものをご利用下さい。 【重要な指定】 ※目を惹きクリックされるインパクトのあるバナーをお願い致します。 サイト内で使用するものなので「こちらをクリック」「詳細はこちら」などのフレーズはなしでお願いいたします。 ・添付画像をご使用ください ・添付画像は反転しないで下さい 【ご注意】 ※他で登録されているデザインや商標の転用など、他社の知的財産権を侵すことNG ※他のクライアントへ既に提案した内容の転用などNG ※ご提案頂きましたバナー案について、SNSへの投稿・Webサイトへのアップ等NG →ポートフォリオ・コンペ提案作品一覧にもアップNGです。 アップする際には、社名を削除し、写真はフリー素材に差し替えてください。 ※今後、画像を再利用する可能性がございます。 ※WEBサイトで他の求人に使用することがあります。 【対応時間】 平日:9時半~18時半 その他ご質問、ご不明点等ありましたら、気軽にお問い合わせください。 見やすく、素敵なデザインをお待ちしております! |
どの案も素敵でしたが、こちらの作品が一番イメージに合っておりました。
皆様ご提案ありがとうございました。どれも個性的でよい提案ばかりでした。また機会がありましたら依頼させていただきますのでよろしくお願いします。

```html
<!DOCTYPE html>
<html lang="ja">
<head>
<meta charset="utf-8">
<title>6tドライバー募集</title>
<link href="https://fonts.googleapis.com/css2?family=Noto+Sans+JP:wght@700;900&display=swap" rel="stylesheet">
<style>
  :root {
    --navy: #0d2a6b;
    --navy-band: #10307a;
    --white: #ffffff;
    --red: #e3172d;
    --yellow: #ffe21a;
    --sky-top: #e9eef4;
    --sky-mid: #b9cbe0;
    --blue-deep: #2f6fc4;
  }
  html, body { margin: 0; padding: 0; overflow: hidden; }
  body { width: 1200px; height: 800px; }
  .banner {
    position: relative;
    width: 1200px;
    height: 800px;
    overflow: hidden;
    font-family: "Noto Sans JP", sans-serif;
  }
  .photo {
    position: absolute; inset: 0;
    background:
      linear-gradient(90deg, rgba(255,255,255,0) 55%, rgba(245,247,250,0.9) 75%, rgba(230,235,242,0.9) 100%),
      linear-gradient(180deg, var(--sky-top) 0%, var(--sky-mid) 45%, #6f9fd6 75%, var(--blue-deep) 100%);
  }
  .photo-people {
    position: absolute;
    left: 720px; top: 230px; width: 480px; height: 570px;
    background: linear-gradient(180deg, #3a4d78 0%, #23345e 60%, #1f3160 100%);
    border-radius: 120px 120px 0 0;
    opacity: 0.85;
  }
  .overlay {
    position: absolute; inset: 0;
    background: linear-gradient(90deg, rgba(47,111,196,0.55) 0%, rgba(47,111,196,0.25) 45%, rgba(47,111,196,0) 65%);
  }
  .band {
    position: absolute;
    left: 20px;
    display: flex;
    align-items: center;
    font-weight: 900;
    letter-spacing: 0;
    white-space: nowrap;
  }
  .band--navy { background: var(--navy-band); color: var(--white); }
  .band--first { top: 10px; height: 90px; padding: 0 24px 0 20px; font-size: 62px; }
  .band--second { top: 110px; height: 90px; padding: 0 24px 0 20px; font-size: 64px; }
  .band--white { top: 224px; height: 80px; padding: 0 26px 0 20px; background: var(--white); color: var(--navy); font-size: 60px; }
  .check-icon { width: 56px; height: 56px; margin-right: 14px; }
  .headline { position: absolute; left: 0; top: 0; width: 1200px; height: 800px; }
  .headline text { font-family: "Noto Sans JP", sans-serif; font-weight: 900; paint-order: stroke fill; stroke-linejoin: round; }
  .title { fill: var(--red); stroke: var(--white); stroke-width: 16px; font-size: 128px; }
  .salary-label { fill: var(--navy); stroke: var(--white); stroke-width: 12px; font-size: 84px; }
  .salary-number { fill: var(--yellow); stroke: var(--red); stroke-width: 14px; font-size: 290px; }
  .salary-number-outer { fill: none; stroke: var(--white); stroke-width: 30px; font-size: 290px; }
  .salary-unit { fill: var(--red); stroke: var(--white); stroke-width: 10px; font-size: 54px; }
</style>
</head>
<body>
<div class="banner">
  <div class="photo" role="img" aria-label="白い大型トラックの前で笑顔で並ぶ作業服姿の男性ドライバー2人の写真">
    <div class="photo-people"></div>
  </div>
  <div class="overlay"></div>

  <div class="band band--navy band--first">
    <svg class="check-icon" viewBox="0 0 56 56" aria-hidden="true">
      <rect x="5" y="9" width="40" height="40" fill="none" stroke="#fff" stroke-width="5"/>
      <path d="M14 28 L24 38 L50 8" fill="none" stroke="#fff" stroke-width="6" stroke-linecap="square"/>
    </svg>
    固定ルート＋体力負担なし
  </div>
  <div class="band band--navy band--second">＋無理な運転はさせない社風</div>
  <div class="band band--white">＝長く働ける環境です！</div>

  <svg class="headline" viewBox="0 0 1200 800" aria-label="6tドライバー募集 月給35万円可能">
    <g transform="skewX(-8)">
      <text class="title" x="100" y="485">6tドライバー募集</text>
      <text class="salary-label" x="150" y="700">月給</text>
      <text class="salary-number-outer" x="380" y="770">35</text>
      <text class="salary-number" x="380" y="770">35</text>
      <text class="salary-unit" x="760" y="655">万円</text>
      <text class="salary-unit" x="760" y="720">可能</text>
    </g>
  </svg>
</div>
</body>
</html>
```